Building Company Business Card Design

Need a design for a business card:
It needs to have: Name, Phone, Facebook link, Website, email
i would also like a list of works we undertake:
-New Homes
-Extensions, Renovations & Bathrooms
-Decking, Carports, Sheds (Residential and Industrial)
-Carpentry
-Fences, Patios & Pergolas

Contact Information for Business Card

Name, Phone, Facebook link, Website, email + details of services provided listed in description

```html
<!DOCTYPE html>
<html lang="en">
<head>
<meta charset="utf-8">
<title>Ridgeline Homes – Business Card</title>
<link rel="stylesheet" href="https://fonts.googleapis.com/css2?family=Montserrat:wght@400;500;600;700&display=swap">
<style>
  :root {
    --green: #3bb54a;
    --ink: #1c1c1c;
    --grey: #8a8a8a;
    --paper: #ffffff;
    --night: #0b0b0c;
    --backdrop: #cfcfcf;
  }
  * { box-sizing: border-box; margin: 0; padding: 0; }
  html, body {
    width: 1200px; height: 815px; overflow: hidden;
    background: var(--backdrop);
    font-family: "Montserrat", sans-serif;
  }
  .sheet {
    width: 1200px; height: 815px;
    display: flex; flex-direction: column; align-items: center; justify-content: center;
    gap: 30px;
  }
  .card {
    position: relative;
    width: 640px; height: 366px;
    border-radius: 22px;
    overflow: hidden;
    box-shadow: 0 10px 24px rgba(0,0,0,.18);
  }

  /* Front */
  .card--front { background: var(--paper); color: var(--ink); }
  .name-tab {
    position: absolute; right: 0; top: 34px;
    width: 34px; height: 34px; background: var(--green);
  }
  .person {
    position: absolute; right: 48px; top: 30px; text-align: right;
  }
  .person__name {
    color: var(--green); font-weight: 700; font-size: 30px; letter-spacing: 2px; line-height: 1.1;
  }
  .person__role {
    font-size: 13px; font-weight: 500; letter-spacing: 2px; color: var(--ink); margin-top: 4px;
  }
  .divider {
    position: absolute; left: 210px; right: 150px; top: 104px;
    height: 2px; background: var(--green);
  }
  .brand {
    position: absolute; display: flex; align-items: flex-start; gap: 10px;
  }
  .brand__mark { width: 16px; height: 16px; background: var(--green); margin-top: 6px; flex: none; }
  .brand__name {
    font-weight: 600; letter-spacing: 1.5px; line-height: 1.15;
  }
  .card--front .brand { left: 40px; top: 150px; }
  .card--front .brand__name { color: var(--ink); font-size: 24px; }
  .card--front .brand__name small { display: block; font-size: 13px; letter-spacing: 1.6px; }

  .contacts {
    position: absolute; left: 330px; top: 200px;
    list-style: none; display: flex; flex-direction: column; gap: 12px;
    font-size: 16px; font-weight: 500; color: var(--ink);
  }
  .contacts li { display: flex; align-items: center; gap: 12px; }
  .contacts svg { width: 16px; height: 16px; flex: none; }
  .contacts .dot { width: 14px; height: 14px; border-radius: 50%; background: var(--green); flex: none; margin: 0 1px; }

  /* Back */
  .card--back { background: var(--night); color: var(--paper); }
  .card--back .brand {
    left: 50%; top: 92px; transform: translateX(-50%);
  }
  .card--back .brand__mark { width: 22px; height: 22px; margin-top: 8px; }
  .card--back .brand__name { color: var(--paper); font-size: 38px; letter-spacing: 2px; }
  .card--back .brand__name small { display: block; font-size: 19px; letter-spacing: 2.4px; }
  .services {
    position: absolute; left: 0; right: 0; top: 252px;
    display: flex; flex-direction: column; align-items: center; gap: 12px;
    font-size: 15px; font-weight: 500; letter-spacing: .6px;
  }
  .services__row { display: flex; gap: 18px; list-style: none; }
  .services__row li { display: flex; align-items: center; gap: 8px; }
  .services__row li::before {
    content: ""; width: 9px; height: 9px; background: var(--green); display: inline-block;
  }
</style>
</head>
<body>
<main class="sheet">
  <section class="card card--front" aria-label="Business card front">
    <span class="name-tab"></span>
    <div class="person">
      <p class="person__name">DAREN HOLT</p>
      <p class="person__role">MANAGER</p>
    </div>
    <span class="divider"></span>
    <div class="brand">
      <span class="brand__mark"></span>
      <p class="brand__name">RIDGELINE HOMES<small>AND DEVELOPMENTS PTY LTD</small></p>
    </div>
    <ul class="contacts">
      <li>
        <svg viewBox="0 0 24 24" aria-hidden="true"><path fill="#3bb54a" d="M6.6 10.8a15.1 15.1 0 0 0 6.6 6.6l2.2-2.2a1 1 0 0 1 1-.25 11.4 11.4 0 0 0 3.6.57 1 1 0 0 1 1 1V20a1 1 0 0 1-1 1A17 17 0 0 1 3 4a1 1 0 0 1 1-1h3.5a1 1 0 0 1 1 1c0 1.25.2 2.45.57 3.57a1 1 0 0 1-.25 1z"/></svg>
        (312)555-0142
      </li>
      <li>
        <svg viewBox="0 0 24 24" aria-hidden="true"><rect x="2" y="5" width="20" height="14" rx="1" fill="#3bb54a"/><path d="M2 6l10 7 10-7" stroke="#fff" stroke-width="1.6" fill="none"/></svg>
        info@youremail.com
      </li>
      <li>
        <svg viewBox="0 0 24 24" aria-hidden="true"><circle cx="12" cy="12" r="10" fill="#3bb54a"/><path d="M2 12h20M12 2c3 3 3 17 0 20M12 2c-3 3-3 17 0 20" stroke="#fff" stroke-width="1.3" fill="none"/></svg>
        www.yourwebsite.com
      </li>
      <li><span class="dot"></span>@your facebook link</li>
    </ul>
  </section>

  <section class="card card--back" aria-label="Business card back">
    <div class="brand">
      <span class="brand__mark"></span>
      <p class="brand__name">RIDGELINE HOMES<small>AND DEVELOPMENTS PTY LTD</small></p>
    </div>
    <div class="services">
      <ul class="services__row">
        <li>New Homes</li>
        <li>Extensions, Renovations &amp; Bathrooms</li>
      </ul>
      <ul class="services__row">
        <li>Decking, Carports, Sheds</li>
        <li>Carpentry</li>
        <li>Fences, Patios &amp; Pergolas</li>
      </ul>
    </div>
  </section>
</main>
</body>
</html>
```